Business Card Design Project

I need some business cards with the logo you did for us (attached)
I am looking for a coulourful yet serious business card

We do market research
on the back I want the logo

on the front my name : Corinne Vasseur
position : Manager
address : Plume Analytics Sarl - 24 Rue des tilleuls
1285 Bellerive - Switzerland
corinne.vasseur@plumeanalytics.ch
Tel : +4122 555 04 87
Mob France :+33 655 52 8014
Mob Italy +39 345 550 2876

The tree of the logo could also be used alone

THE BACKGROUND COLOR ON THE FRONT HAS TO BE WHITE, ON THE BACK YU CAN TRY OHER COLOUR BUT HOMOGENEOUS (NOT EXPENSIVE TO PRINT)

Target Market(s)

multinational companies or other market research companies

Industry/Entity Type

Market Research

Requirements
Must have
• logo on the back
and all the info above

```html
<!DOCTYPE html>
<html lang="en">
<head>
<meta charset="utf-8">
<title>Plume Analytics – Business Card</title>
<link rel="stylesheet" href="https://fonts.googleapis.com/css2?family=Arimo:wght@400;700&display=swap">
<style>
  :root {
    --backdrop: #e4e4e6;
    --card: #ffffff;
    --ink: #c8174f;
    --ink-soft: #d23a68;
    --mark: #e7a9c0;
    --shadow: rgba(0, 0, 0, 0.18);
  }
  html, body {
    margin: 0;
    padding: 0;
    width: 1200px;
    height: 880px;
    overflow: hidden;
    background: var(--backdrop);
    font-family: "Arimo", Arial, sans-serif;
  }
  .canvas {
    position: relative;
    width: 1200px;
    height: 880px;
    display: flex;
    align-items: center;
    justify-content: center;
    gap: 60px;
  }
  .card {
    position: relative;
    width: 510px;
    height: 330px;
    background: var(--card);
    box-shadow: 0 10px 28px var(--shadow);
    box-sizing: border-box;
    color: var(--ink);
  }

  /* Front */
  .card--front { padding: 34px 38px; }
  .brand {
    display: flex;
    align-items: center;
    gap: 10px;
  }
  .brand__dot {
    width: 30px;
    height: 30px;
    border-radius: 50%;
    background: var(--mark);
  }
  .brand__name {
    font-size: 26px;
    font-weight: 400;
    color: var(--ink);
    letter-spacing: 0.2px;
  }
  .person { margin-top: 30px; }
  .person__name {
    font-size: 19px;
    font-weight: 700;
    margin: 0;
  }
  .person__role {
    font-size: 12px;
    font-weight: 700;
    margin: 3px 0 0;
  }
  .address {
    margin-top: 16px;
    font-size: 12.5px;
    line-height: 1.35;
    font-style: normal;
  }
  .contacts {
    margin: 14px 0 0;
    padding: 0;
    list-style: none;
    font-size: 12.5px;
    line-height: 1.4;
  }

  /* Back */
  .card--back {
    display: flex;
    flex-direction: column;
    align-items: center;
    justify-content: center;
    gap: 14px;
  }
  .card--back .brand__dot { width: 56px; height: 56px; }
  .card--back .brand__name { font-size: 42px; }
  .website {
    font-size: 13px;
    font-weight: 700;
    color: var(--ink-soft);
    margin-left: 120px;
  }
</style>
</head>
<body>
  <main class="canvas">
    <section class="card card--front" aria-label="Card front">
      <div class="brand">
        <span class="brand__dot"></span>
        <span class="brand__name">Plume Analytics</span>
      </div>
      <div class="person">
        <p class="person__name">Corinne Vasseur</p>
        <p class="person__role">Manager</p>
      </div>
      <address class="address">
        Plume Analytics Sarl - 24 Rue des tilleuls<br>
        1285 Bellerive - Switzerland
      </address>
      <ul class="contacts">
        <li>tel : +4122 555 04 87</li>
        <li>mob france : +33 655 52 8014</li>
        <li>mob italy : +39 345 550 2876</li>
        <li>email : corinne.vasseur@plumeanalytics.ch</li>
      </ul>
    </section>

    <section class="card card--back" aria-label="Card back">
      <div class="brand">
        <span class="brand__dot"></span>
        <span class="brand__name">Plume Analytics</span>
      </div>
      <span class="website">www.plumeanalytics.ch</span>
    </section>
  </main>
</body>
</html>
```